Business card design needed

Need a business card for a new Company in Melbourne called Brightway Lending Choices. This company is a Mortgage Brokering company that facilitates mainly Residential loans, but also Business and Commercial loans.
I would like something professional as I am in the finance industry.
I would like Brightway Lending font wise to be bigger than choices, with the word choices to sit below the Brightway Lending.

Industry/Entity Type

Finance

Contact Information for Business Card

Daniel Westhorpe | Lending Specialist
Brightway Lending Choices
P.O Box 517 Elmvale Vic.3071
T. +61 3 9000 4171 | F. +61 3 9000 6235| M. +61 400572904
www.brightwaylending.example

Daniel Westhorpe is a credit representative (CRN 572914)of KRVMO Pty.Ltd (Australian Credit Licence No 648502)

Requirements
Must have
• Daniel Westhorpe is a credit representative (CRN 572914)of KRVMO Pty.Ltd (Australian Credit Licence No 648502) has to sit at the bottom of the card, in the smallest readable font.

The logo to be designed is the most crucial thing for me.

```html
<!DOCTYPE html>
<html lang="en">
<head>
<meta charset="utf-8">
<title>Brightway Lending Choices – Business Card</title>
<link rel="stylesheet" href="https://fonts.googleapis.com/css2?family=Alegreya:wght@400&family=Questrial&family=Crimson+Text&display=swap">
<style>
  :root {
    --ink: #000000;
    --paper: #ffffff;
    --blue-deep: #0b2a4a;
    --blue-mid: #2f7fc0;
    --blue-light: #a9d3f0;
    --fine-ink: #0a0a0a;
  }
  * { margin: 0; padding: 0; box-sizing: border-box; }
  html, body {
    width: 1200px; height: 741px; overflow: hidden;
    background: var(--ink);
  }
  .card {
    position: relative;
    width: 1200px; height: 741px;
    background: var(--ink);
    color: var(--paper);
    font-family: "Questrial", sans-serif;
    overflow: hidden;
  }
  .card__photo {
    position: absolute; inset: 0;
    width: 1200px; height: 741px;
  }
  .brand {
    position: absolute;
    left: 82px; top: 58px;
    display: inline-flex;
    align-items: flex-start;
    gap: 14px;
  }
  .brand__dot {
    width: 26px; height: 26px;
    border-radius: 50%;
    background: var(--paper);
    margin-top: 20px;
  }
  .brand__words { display: inline-block; text-align: right; }
  .brand__name {
    font-family: "Alegreya", serif;
    font-size: 62px;
    line-height: 1;
    letter-spacing: 0.5px;
  }
  .brand__sub {
    font-family: "Questrial", sans-serif;
    font-size: 46px;
    line-height: 1;
    margin-top: 4px;
  }
  .rule {
    position: absolute;
    left: 82px; top: 213px;
    width: 924px; height: 3px;
    background: var(--paper);
  }
  .person {
    position: absolute;
    left: 80px; top: 262px;
  }
  .person__name { font-size: 42px; line-height: 1.15; }
  .person__role { font-size: 31px; line-height: 1.2; }
  .contact {
    position: absolute;
    left: 80px; top: 445px;
    list-style: none;
    font-size: 33px;
    line-height: 47.5px;
  }
  .disclosure {
    position: absolute;
    right: 57px; top: 570px;
    width: 240px;
    text-align: right;
    font-family: "Crimson Text", serif;
    font-size: 19.5px;
    line-height: 24.5px;
    color: var(--fine-ink);
  }
</style>
</head>
<body>
<main class="card">
  <svg class="card__photo" viewBox="0 0 1200 741" role="img" aria-label="Photo of blue hanging file folders with a tab labelled for mortgages">
    <defs>
      <radialGradient id="folderGlow" cx="1080" cy="600" r="620" gradientUnits="userSpaceOnUse">
        <stop offset="0" stop-color="var(--blue-light)"/>
        <stop offset="0.35" stop-color="var(--blue-mid)"/>
        <stop offset="0.7" stop-color="var(--blue-deep)"/>
        <stop offset="1" stop-color="var(--ink)" stop-opacity="0"/>
      </radialGradient>
    </defs>
    <polygon points="640,741 700,330 1000,190 1200,110 1200,741" fill="url(#folderGlow)"/>
  </svg>

  <header class="brand">
    <span class="brand__dot"></span>
    <span class="brand__words">
      <span class="brand__name">Brightway Lending</span><br>
      <span class="brand__sub">CHOICES</span>
    </span>
  </header>

  <div class="rule"></div>

  <section class="person">
    <h1 class="person__name">Daniel Westhorpe</h1>
    <p class="person__role">Lending Specialist</p>
  </section>

  <ul class="contact">
    <li>P.O. Box 517 Elmvale Vic.3071</li>
    <li>T. +61 3 9000 4171</li>
    <li>F. +61 3 9000 6235</li>
    <li>M. +61 400572904</li>
    <li>www.brightwaylending.example</li>
  </ul>

  <p class="disclosure">Daniel Westhorpe is a credit representative (CRN 572914) of KRVMO Pty. Ltd (Australian Credit Licence No 648502)</p>
</main>
</body>
</html>
```